Hvac and insulation company needs good looking business card design

We are hvac and insulation company and looking for a new business cards that look to today standards designs

Target Market(s)

homeowners

Industry/Entity Type

Hvac

Contact Information for Business Card

Name: Dorian Velkova
Home comfort consultant
address: 4827 Marrow Ridge Rd #215 Oakland, CA 94611
office: 888-317-5069
cell: 510-642-1388
Lic.# 458127
Email: dorian@quarry-hvac.com
Web: quarry-hvac.com

Requirements
Must have
• clean and sleek look
Nice to have
• simple with a clean look
Should not have
• to busy business card

```html
<!DOCTYPE html>
<html lang="en">
<head>
<meta charset="utf-8">
<title>Quarry – Business Card</title>
<link href="https://fonts.googleapis.com/css2?family=Roboto:wght@400;500&family=Roboto+Condensed:wght@400;700&display=swap" rel="stylesheet">
<style>
  :root {
    --backdrop: #151515;
    --card: #e3e2e0;
    --ink: #111111;
    --brand: #ef6a28;
  }
  * { margin: 0; padding: 0; box-sizing: border-box; }
  html, body { width: 1200px; height: 1200px; overflow: hidden; background: var(--backdrop); }
  .card {
    position: absolute; left: 179px; width: 840px; height: 480px;
    background: var(--card); color: var(--ink);
    font-family: "Roboto Condensed", "Arial Narrow", sans-serif;
  }
  .card--front { top: 96px; }
  .card--back { top: 634px; }
  .rule { position: absolute; height: 3px; background: var(--ink); }
  .brand {
    position: absolute; display: flex; align-items: center; gap: 16px;
    font-family: "Roboto", Arial, sans-serif; font-weight: 500;
    color: var(--brand); line-height: 1; letter-spacing: 0.5px;
  }
  .brand--front { left: 258px; top: 187px; height: 80px; font-size: 80px; }
  .brand--front .brand-mark { width: 80px; height: 80px; }
  .brand--back { left: 42px; top: 172px; height: 68px; font-size: 76px; gap: 14px; }
  .brand--back .brand-mark { width: 68px; height: 68px; }
  .brand-mark { background: var(--brand); display: block; flex: none; }
  .front-web {
    position: absolute; left: 0; right: 0; top: 415px;
    display: flex; justify-content: center; align-items: center; gap: 12px;
    font-size: 25px; letter-spacing: -0.3px;
  }
  .front-web svg { width: 37px; height: 37px; }
  .person { position: absolute; right: 77px; top: 122px; text-align: right; }
  .person-name { font-weight: 700; font-size: 43px; line-height: 1; letter-spacing: -0.5px; }
  .person-role { font-size: 20px; margin-top: 6px; }
  .contact { position: absolute; right: 77px; text-align: right; font-size: 23px; line-height: 1.2; white-space: nowrap; }
  .contact--address { top: 226px; line-height: 1.27; }
  .contact--online { top: 289px; line-height: 1.05; }
  .contact--phones { top: 351px; line-height: 1.02; }
  .contact--license { top: 419px; font-size: 21px; }
  .phone-row span { display: inline-block; margin-right: 14px; }
  .icon {
    position: absolute; left: 770px; width: 34px; height: 36px;
    background: var(--ink); border-radius: 10px;
    display: flex; align-items: center; justify-content: center; color: #fff;
  }
  .icon svg { width: 22px; height: 22px; }
  .icon--text { font-size: 15px; font-weight: 400; }
</style>
</head>
<body>

<section class="card card--front">
  <div class="rule" style="left:0;width:247px;top:235px"></div>
  <div class="rule" style="left:596px;right:0;top:235px"></div>
  <div class="brand brand--front"><span class="brand-mark"></span>quarry</div>
  <div class="front-web">
    <svg viewBox="0 0 40 40" fill="none" stroke="#111" stroke-width="2">
      <circle cx="20" cy="20" r="17"/><ellipse cx="20" cy="20" rx="8" ry="17"/>
      <line x1="3" y1="20" x2="37" y2="20"/><line x1="20" y1="3" x2="20" y2="37"/>
      <path d="M6 11h28M6 29h28"/>
    </svg>
    <span>www.quarry-hvac.com</span>
  </div>
</section>

<section class="card card--back">
  <div class="rule" style="left:0;width:29px;top:207px"></div>
  <div class="rule" style="left:378px;width:385px;top:207px"></div>
  <div class="rule" style="left:785px;right:0;top:207px"></div>
  <div class="brand brand--back"><span class="brand-mark"></span>quarry</div>

  <div class="person">
    <div class="person-name">Dorian Velkova</div>
    <div class="person-role">Home Comfort Consultant</div>
  </div>

  <div class="contact contact--address">4827 Marrow Ridge Rd #215<br>Harlow Springs, CA 94716</div>
  <div class="contact contact--online">dorian@quarry-hvac.com<br>www.quarry-hvac.com</div>
  <div class="contact contact--phones">
    <div class="phone-row"><span>Office:</span>888-317-5069</div>
    <div class="phone-row"><span>Cell:</span>510-642-1388</div>
  </div>
  <div class="contact contact--license">Lic.# 458127</div>

  <div class="icon" style="top:236px">
    <svg viewBox="0 0 24 24" fill="none" stroke="#fff" stroke-width="1.6"><path d="M3 11l9-7 9 7"/><path d="M5 10v10h14V10"/><rect x="10" y="14" width="4" height="6"/></svg>
  </div>
  <div class="icon" style="top:294px">
    <svg viewBox="0 0 24 24" fill="none" stroke="#fff" stroke-width="1.4"><circle cx="12" cy="12" r="9"/><ellipse cx="12" cy="12" rx="4" ry="9"/><path d="M3 12h18M4.5 7.5h15M4.5 16.5h15"/></svg>
  </div>
  <div class="icon" style="top:356px">
    <svg viewBox="0 0 24 24" fill="none" stroke="#fff" stroke-width="1.4"><path d="M3 9c0-3 18-3 18 0v2h-4V9H7v2H3z"/><path d="M6 12h12l2 7H4z"/><circle cx="12" cy="15.5" r="2"/></svg>
  </div>
  <div class="icon icon--text" style="top:412px">LIC</div>
</section>

</body>
</html>
```